Business branding (card, web design) needed for Remedial / Sports massage

I need a clean, fresh design for my sports massage business called Brightwell-Motion.

I work with high profile professional sports teams (massage, clinical tapeing, health assessments, pilates, coaching) however would like to expand into the entertainment market so need a design that would appeal to both.
NO LOTUS FLOWERS, HANDS OR YOGA POSES FOR DESIGNS

The successful brand design will need to be scalable (e.g. resolution/sizing) to work holistically across my website, marketing collateral and clothing.

Colour pallets that appeal to me - Black, white, blue, green, taupe,
and would prefer clean crisp designs that evoke professionalism, continuous improvement, flow and balance.

Good Luck, can't wait to find my new brand... :)
Updates

I have uploaded a business card that I do like,  See if you can be creative with the logo

Thanks

Target Market(s)

professional sports teams / athletes, and entertainment professionals.

I HAVE UPLOADED A PDF OF WHAT I HAVE DONE. YOU MAY USE LOGO BUT BE CREATIVE PLEASE.

Industry/Entity Type

Entertainment

Contact Information for Business Card

Brightwell-Motion
'Recover Stronger' (strap line)

Colette Farrow
Director / Remedial Massage

0417263950
212 Larkmore Street
Kelbridge, VIC 3261

www.brightwell-motion.com.au
info@brightwell-motion.com.au

Logo Text

Brightwell-Motion

Logo styles of interest
Pictorial/Combination Logo
Abstract Logo
Requirements
Should not have
• FLOWERS

```html
<!DOCTYPE html>
<html lang="en">
<head>
<meta charset="utf-8">
<title>Brightwell-Motion — Business Card</title>
<link rel="stylesheet" href="https://fonts.googleapis.com/css2?family=Arimo:wght@400;700&display=swap">
<style>
  :root {
    --card-bg: #ffffff;
    --ink: #0b0b0b;
    --emblem-grey: #c3c2c3;
    --tagline-blue: #6cc3e8;
    --brand-dot: #050708;
  }
  * { margin: 0; padding: 0; box-sizing: border-box; }
  html, body {
    width: 1200px;
    height: 686px;
    overflow: hidden;
    background: var(--card-bg);
  }
  .card {
    position: relative;
    width: 1200px;
    height: 686px;
    overflow: hidden;
    background: var(--card-bg);
    font-family: "Arimo", Arial, sans-serif;
    color: var(--ink);
  }
  .emblem-area {
    position: absolute;
    left: 523px;
    top: -2px;
    width: 862px;
    height: 862px;
    border-radius: 50%;
    background: var(--emblem-grey);
  }
  .brand {
    position: absolute;
    left: 18px;
    top: 97px;
    width: 400px;
    text-align: center;
  }
  .brand-dot {
    display: block;
    width: 206px;
    height: 206px;
    margin: 0 auto;
    border-radius: 50%;
    background: var(--brand-dot);
  }
  .brand-name {
    margin-top: 24px;
    font-weight: 700;
    font-size: 39px;
    line-height: 1;
    letter-spacing: 0.2px;
  }
  .brand-tagline {
    margin-top: 14px;
    font-size: 24px;
    line-height: 1.1;
    color: var(--tagline-blue);
    letter-spacing: 0.5px;
  }
  .address {
    position: absolute;
    left: 80px;
    top: 480px;
    font-size: 30px;
    line-height: 40px;
    font-style: normal;
  }
  .person {
    position: absolute;
    right: 78px;
    top: 92px;
    text-align: right;
  }
  .person-name {
    font-weight: 400;
    font-size: 71px;
    line-height: 1;
  }
  .person-role {
    margin-top: 12px;
    font-size: 33px;
    line-height: 1.1;
  }
  .contact {
    position: absolute;
    right: 78px;
    top: 473px;
    text-align: right;
    font-size: 30px;
    line-height: 40.5px;
    font-style: normal;
  }
</style>
</head>
<body>
  <main class="card">
    <div class="emblem-area" role="img" aria-label="Large soft grey brand emblem backdrop"></div>

    <section class="brand">
      <span class="brand-dot" aria-hidden="true"></span>
      <h1 class="brand-name">Brightwell-Motion</h1>
      <p class="brand-tagline">‘Recover Stronger’</p>
    </section>

    <address class="address">
      212 Larkmore Street<br>
      Kelbridge<br>
      Vic 3261
    </address>

    <header class="person">
      <h2 class="person-name">Colette Farrow</h2>
      <p class="person-role">Director / Remedial Massage</p>
    </header>

    <address class="contact">
      0417263950<br>
      info@brightwell-motion.com.au<br>
      www.brightwell-motion.com.au
    </address>
  </main>
</body>
</html>
```